Business Card Design Project - 2 sided

We need a business card design for a card having one business on each side (ie. two businesses on one card). Would like a design that incorporates logo, tagline and normal fields (name, position, address, phone).

Would also like an allowance for small font text along the bottom (text to be determined, but less than 50 characters).

NB. Attached logo for Verbica Partners has two variations - either can be used.

www.verbicapartners.com / www.kelvarho.com

```html
<!DOCTYPE html>
<html lang="en">
<head>
<meta charset="utf-8">
<title>Verbica Partners / Kelvarho – Business Card</title>
<link rel="stylesheet" href="https://fonts.googleapis.com/css2?family=Tinos&family=Noto+Sans&display=swap">
<style>
  :root {
    --backdrop: #999999;
    --card: #ffffff;
    --shadow: rgba(0, 0, 0, 0.75);
    --rule-green: #8dc63f;
    --kelvarho-blue: #1d7fa6;
    --verbica-navy: #1f1a6b;
  }
  html, body {
    margin: 0;
    padding: 0;
    width: 1200px;
    height: 1200px;
    overflow: hidden;
    background: var(--backdrop);
  }
  .canvas {
    position: relative;
    width: 1200px;
    height: 1200px;
  }
  .card {
    position: absolute;
    left: 210px;
    width: 780px;
    height: 444px;
    background: var(--card);
    border-radius: 45px;
    box-shadow: 9px 9px 6px var(--shadow);
  }
  .card--kelvarho { top: 78px; color: var(--kelvarho-blue); }
  .card--verbica  { top: 678px; color: var(--verbica-navy); }

  .brand {
    position: absolute;
    left: 30px;
    width: 335px;
    top: 0;
    height: 444px;
    display: flex;
    align-items: center;
    justify-content: center;
    gap: 14px;
  }
  .brand__dot {
    width: 58px;
    height: 58px;
    border-radius: 50%;
    background: var(--rule-green);
    flex: none;
  }
  .brand__name {
    font-family: "Tinos", "Times New Roman", serif;
    font-size: 58px;
    line-height: 1;
    white-space: nowrap;
  }
  .card--verbica .brand__name { font-size: 40px; }

  .divider {
    position: absolute;
    left: 386px;
    top: 94px;
    width: 3px;
    height: 256px;
    background: var(--rule-green);
  }

  .details {
    position: absolute;
    left: 418px;
    top: 116px;
  }
  .details__name {
    font-family: "Tinos", "Times New Roman", serif;
    font-size: 55px;
    line-height: 1;
    margin: 0;
    font-weight: normal;
  }
  .details__position {
    font-family: "Tinos", "Times New Roman", serif;
    font-size: 39px;
    line-height: 1;
    margin: 4px 0 0;
  }
  .details__contact {
    font-family: "Noto Sans", "Segoe UI", sans-serif;
    font-size: 20px;
    line-height: 21px;
    margin: 34px 0 0;
    padding: 0;
    list-style: none;
  }
</style>
</head>
<body>
<main class="canvas">
  <section class="card card--kelvarho" aria-label="Kelvarho side">
    <div class="brand">
      <span class="brand__dot" aria-hidden="true"></span>
      <span class="brand__name">Kelvarho</span>
    </div>
    <div class="divider"></div>
    <div class="details">
      <h2 class="details__name">John Doe</h2>
      <p class="details__position">position</p>
      <ul class="details__contact">
        <li>Website: www.kelvarho.com</li>
        <li>Phone Number: 012345678</li>
        <li>Address: 123 Rd My Address</li>
      </ul>
    </div>
  </section>

  <section class="card card--verbica" aria-label="Verbica Partners side">
    <div class="brand">
      <span class="brand__name">Verbica Partners</span>
    </div>
    <div class="divider"></div>
    <div class="details">
      <h2 class="details__name">John Doe</h2>
      <p class="details__position">position</p>
      <ul class="details__contact">
        <li>Website: www.verbicapartners.com</li>
        <li>Phone Number: 012345678</li>
        <li>Address: 123 Rd My Address</li>
      </ul>
    </div>
  </section>
</main>
</body>
</html>
```